Elmrow Management real estate management company needs presentation folder to hand clients

looking for a folder with pockets that represent my real estate management company when i hand to client reports or promotional material. I only do resedential real estate. I want classy and professional - pictures or additioal graphixs are fine

when a client open i will usally insert text and reports about my business
also on the inside flap is usally place for my business card i will upload a picture so the theme can be constant

Target Market(s)

my existing real estate cleints
and i will use when i am soliciting new business

Industry/Entity Type

Real Estate

Font styles to use
Serif

Requirements
Must have
• must have logo
• must give appearance of professionalism and maturity
• have basic company info tel# ,address
• id like viewer to know I manage real estate - focus on residential small to large apartment buildings
• not strip malls, not giganic complexes - im a mid size company
• logo is black but i welcome color as u see fit
Nice to have
• maybe pictures
• my slogan - " we will manage your building like its our own "
• focus on professioanl, safe, trust worthy
• type style should be clear and readable - but im open to sugestions

```html
<!DOCTYPE html>
<html lang="en">
<head>
<meta charset="utf-8">
<title>Elmrow Management – Presentation Folder</title>
<link href="https://fonts.googleapis.com/css2?family=Open+Sans:wght@400;600;700;800&display=swap" rel="stylesheet">
<style>
  :root {
    --folder-blue: #0d5288;
    --tab-blue: #1a73b9;
    --watermark-blue: #1f64a0;
    --paper: #ffffff;
    --text-light: #ffffff;
  }
  html, body {
    margin: 0;
    padding: 0;
    overflow: hidden;
    background: var(--paper);
  }
  .folder-spread {
    position: relative;
    width: 1200px;
    height: 999px;
    overflow: hidden;
    background: var(--paper);
    font-family: "Open Sans", Arial, sans-serif;
  }
  .folder-shapes {
    position: absolute;
    inset: 0;
  }
  .cover-watermark-name {
    position: absolute;
    left: 40px;
    top: 330px;
    width: 560px;
    text-align: center;
    color: var(--watermark-blue);
    font-weight: 800;
    font-size: 44px;
    line-height: 1.1;
    letter-spacing: 1px;
    text-transform: uppercase;
    margin: 0;
  }
  .cover-contact {
    position: absolute;
    left: 100px;
    top: 625px;
    color: var(--text-light);
    font-size: 9.5px;
    line-height: 12px;
    font-weight: 600;
    margin: 0;
  }
  .cover-contact .contact-address {
    display: block;
    margin-top: 8px;
    text-transform: uppercase;
  }
  .flap-brand-name {
    position: absolute;
    left: 600px;
    top: 145px;
    width: 520px;
    text-align: center;
    color: var(--folder-blue);
    font-weight: 800;
    font-size: 28px;
    text-transform: uppercase;
    letter-spacing: 1px;
    margin: 0;
  }
  .flap-slogan {
    position: absolute;
    left: 600px;
    top: 291px;
    width: 517px;
    text-align: center;
    color: var(--text-light);
    font-size: 20.5px;
    font-weight: 600;
    margin: 0;
    line-height: 30px;
  }
</style>
</head>
<body>
<main class="folder-spread">
  <svg class="folder-shapes" width="1200" height="999" viewBox="0 0 1200 999" xmlns="http://www.w3.org/2000/svg">
    <defs>
      <linearGradient id="streetPhotoTones" x1="0" y1="0" x2="0" y2="1">
        <stop offset="0" stop-color="#8fc0e8"/>
        <stop offset="0.35" stop-color="#c9d7e2"/>
        <stop offset="0.65" stop-color="#8c949c"/>
        <stop offset="0.88" stop-color="#6f9a4c"/>
        <stop offset="1" stop-color="#5f8a3e"/>
      </linearGradient>
    </defs>
    <!-- front cover -->
    <rect class="cover-panel" x="40" y="54" width="560" height="647" fill="var(--folder-blue)"/>
    <!-- pockets -->
    <path class="pocket-left" d="M87 702 H598 L574 880 Q566 945 522 945 H87 Z" fill="var(--folder-blue)"/>
    <path class="pocket-right" d="M604 702 H1114 V945 H690 Q646 945 638 880 Z" fill="var(--folder-blue)"/>
    <!-- inside flap band -->
    <polygon class="flap-tab-top" points="600,260 830,260 848,280 600,280" fill="var(--tab-blue)"/>
    <rect class="flap-band" x="600" y="278" width="560" height="314" fill="var(--folder-blue)"/>
    <polygon class="flap-tab-bottom" points="875,590 1160,590 1160,632 908,632" fill="var(--folder-blue)"/>
    <rect class="flap-photo" x="600" y="328" width="560" height="250" fill="url(#streetPhotoTones)"
          role="img" aria-label="Photo of a sunny residential street lined with two-storey houses, porches and flower beds"/>
  </svg>

  <p class="cover-watermark-name">Elmrow<br>Management</p>

  <p class="cover-contact">
    Office tel: 555-014-2287<br>
    email: info@elmrowmgmt.com<br>
    Cell: 555-013-9104
    <span class="contact-address">42 Alder Court Suite 210 Greenhaven NY 10990</span>
  </p>

  <p class="flap-brand-name">Elmrow Management</p>

  <p class="flap-slogan">we will manage your building like its our own</p>
</main>
</body>
</html>
```